Stationery Design Project

We are looking stationary Design for Velbrook International, a high end clothing company. I have attached an image of our Logo below.
Updates
I am looking for designs for the following stationaries:
1. Leather Binders
2. Paper Binders
3. Letterhead
4. Envelopes
5. Pens, pencils etc
We would love to see designs with gold, black and white color combination.
Industry/Entity Type
Clothing
Look and feel
Each slider illustrates characteristics of the customer's brand and the style your logo design should communicate.

```html
<!DOCTYPE html>
<html lang="en">
<head>
<meta charset="utf-8">
<title>Velbrook International — Envelopes</title>
<link rel="stylesheet" href="https://fonts.googleapis.com/css2?family=Bodoni+Moda:wght@500&family=Roboto:wght@300&display=swap">
<style>
  :root {
    --backdrop: #ececec;
    --paper: #f6f6f6;
    --paper-edge: #e2e2e2;
    --ink: #1f1f1f;
    --ink-soft: #3a3a3a;
    --flap: #333333;
    --mark-faint: #5a5a5a;
  }
  html, body {
    margin: 0;
    padding: 0;
    width: 1200px;
    height: 892px;
    overflow: hidden;
    background: var(--backdrop);
  }
  .stationery {
    position: relative;
    width: 1200px;
    height: 892px;
  }
  .envelope {
    position: absolute;
    width: 520px;
    height: 260px;
    background: var(--paper);
    border: 1px solid var(--paper-edge);
    box-shadow: 0 2px 6px rgba(0,0,0,0.08);
    box-sizing: border-box;
    overflow: hidden;
  }
  .envelope--front { left: 50px; top: 316px; }
  .envelope--back  { left: 630px; top: 316px; }

  .brand {
    position: absolute;
    left: 0;
    right: 0;
    top: 58px;
    text-align: center;
    color: var(--ink);
    font-family: "Bodoni Moda", serif;
    font-weight: 500;
  }
  .brand__dot {
    display: block;
    width: 34px;
    height: 34px;
    margin: 0 auto 10px;
    border-radius: 50%;
    border: 1px solid var(--ink-soft);
    box-sizing: border-box;
  }
  .brand__name {
    margin: 0;
    font-size: 26px;
    letter-spacing: 2px;
    line-height: 1;
    text-transform: uppercase;
  }
  .brand__sub {
    margin: 6px 0 0;
    font-size: 8px;
    letter-spacing: 6px;
    text-transform: uppercase;
  }
  .address {
    position: absolute;
    left: 0;
    right: 0;
    top: 170px;
    margin: 0;
    text-align: center;
    font-family: "Roboto", sans-serif;
    font-weight: 300;
    font-size: 9px;
    color: var(--ink);
  }
  .rule {
    position: absolute;
    left: 28px;
    right: 28px;
    bottom: 30px;
    height: 2px;
    background: var(--ink);
  }

  .flap {
    position: absolute;
    left: 0;
    top: 0;
    width: 520px;
    height: 72px;
  }
  .flap__mark {
    position: absolute;
    left: 250px;
    top: 26px;
    width: 20px;
    height: 20px;
    border-radius: 50%;
    border: 1px solid var(--mark-faint);
    box-sizing: border-box;
  }
</style>
</head>
<body>
  <main class="stationery">
    <section class="envelope envelope--front" aria-label="Envelope front">
      <div class="brand">
        <span class="brand__dot"></span>
        <p class="brand__name">Velbrook</p>
        <p class="brand__sub">International</p>
      </div>
      <p class="address">74 Harlow Crest Rd, Ashford Vale, CA 90318</p>
      <div class="rule"></div>
    </section>

    <section class="envelope envelope--back" aria-label="Envelope back">
      <svg class="flap" viewBox="0 0 520 72" aria-hidden="true">
        <path d="M0 0 H520 V56 Q520 72 504 72 H16 Q0 72 0 56 Z" fill="var(--flap)"/>
      </svg>
      <span class="flap__mark"></span>
    </section>
  </main>
</body>
</html>
```